Lien Post Card - (5.5 x 8.5)

FRONT OF POSTCARD
Is a Property Lien Putting Your Home at Risk?
HOA Liens • Tax Liens • Municipal Charges • Other Property-Related Liens
You may have options to resolve outstanding liens and protect your home.
A Refinance or Home Equity Line of Credit (HELOC) may help you:
✔ Pay off qualifying liens
✔ Consolidate debt into one manageable payment
✔ Access your home's equity
✔ Improve your financial flexibility
✔ Avoid additional penalties, fees, or collection actions
Don't wait until the situation becomes more difficult.
Call today for a confidential review of your options.
Bluegate Lending Partners, Inc.
(800) 647-2915 x 42
www.bluegatelendco.com
NMLS #381640
BACK OF POSTCARD
Your Home Equity Could Be the Solution
If you have received notices regarding:
• Delinquent Property Taxes
• HOA or Condo Association Assessments
• Municipal Utility Liens
• Special Assessments
• Other Property-Related Obligations
You may qualify for financing options designed to help satisfy those obligations and bring your property current.
Our experienced mortgage professionals can review your situation and discuss available programs, including:
• Cash-Out Refinancing
• Home Equity Lines of Credit (HELOCs)
• Home Equity Loans
• Debt Consolidation Solutions
Free Consultation • No Obligation
Contact Marcus Delaney today at (800) 647-2915 x42 or mdelaney@bluegatelendco.com (NMLS #57308)

```html
<!DOCTYPE html>
<html lang="en">
<head>
<meta charset="utf-8">
<title>Lien Postcard – Front and Back</title>
<link rel="stylesheet" href="https://fonts.googleapis.com/css2?family=Barlow+Condensed:wght@500;600;700;800&family=Nunito+Sans:wght@400;600;700;800&display=swap">
<style>
  :root{
    --stage:#a7a9ac;
    --navy:#0c2a55;
    --band:#1c4a8c;
    --blue:#1f5fb3;
    --green:#78bc36;
    --green-soft:#a9d35e;
    --ink:#1a2230;
    --white:#ffffff;
    --photo:#c9c2b8;
    --head:"Barlow Condensed", "Arial Narrow", sans-serif;
    --body:"Nunito Sans", Arial, sans-serif;
  }
  *{box-sizing:border-box;margin:0;padding:0}
  html,body{width:869px;height:1200px;overflow:hidden;background:var(--stage)}
  .canvas{position:relative;width:869px;height:1200px;font-family:var(--body);color:var(--ink)}
  .card{position:absolute;left:62px;width:745px;height:481px;background:var(--white);overflow:hidden}
  .card--front{top:110px;background:linear-gradient(180deg,#eef3f8 0%,#ffffff 45%)}
  .card--back{top:631px;height:480px}
  .abs{position:absolute}

  /* brand block */
  .brand{display:flex;align-items:center;gap:6px;font-family:var(--body);font-weight:800;color:var(--navy);line-height:1.15}
  .brand__dot{flex:none;border-radius:50%;background:var(--blue)}

  /* front headline */
  .headline{font-family:var(--head);font-weight:800;text-transform:uppercase;line-height:42px;font-size:50px;color:var(--navy);letter-spacing:.2px;white-space:nowrap}
  .headline .blue{color:var(--blue)}
  .headline .green{color:var(--green)}
  .headline .small{font-size:38px}
  .lien-types{left:223px;top:110px;border-left:2px solid var(--blue);padding-left:14px;font-size:11.6px;line-height:16px;color:var(--ink)}
  .rule{height:2px;background:var(--green)}
  .intro{left:40px;top:166px;font-size:15px;line-height:19px;font-weight:600;color:var(--ink)}
  .intro strong{color:var(--blue);font-weight:800}

  .benefit-panel{left:0;top:215px;width:440px;height:169px;border-radius:0 14px 14px 0;background:linear-gradient(90deg,var(--green-soft) 0%,#c2de86 100%)}
  .benefit-title{left:40px;top:226px;width:207px;font-size:12px;line-height:15px;font-weight:800;color:var(--navy);padding-bottom:4px;border-bottom:1px solid var(--navy);white-space:nowrap}
  .benefit-list{left:40px;top:268px;width:207px;height:98px;list-style:none;font-size:10.6px;line-height:12.5px;color:var(--ink);border-right:1px solid var(--navy);padding-right:8px}
  .benefit-list li{position:relative;padding-left:19px;margin-bottom:4.5px}
  .benefit-list li::before{content:"";position:absolute;left:0;top:1px;width:11px;height:11px;border-radius:50%;background:var(--navy)}
  .benefit-list li::after{content:"";position:absolute;left:3.5px;top:3px;width:3px;height:5px;border:solid var(--white);border-width:0 1.5px 1.5px 0;transform:rotate(45deg)}

  .urgent{left:264px;top:214px;width:158px;height:158px;border-radius:50%;background:var(--navy);border:3px solid var(--blue);display:flex;flex-direction:column;align-items:center;justify-content:center;text-align:center;color:var(--white);font-weight:800;font-size:14px;line-height:17px;padding-top:8px;white-space:nowrap}
  .urgent .green{color:var(--green)}
  .urgent svg{margin-bottom:6px}

  .photo-ring{left:418px;top:128px;width:350px;height:350px;border-radius:50%;border:9px solid var(--blue);border-color:var(--blue) transparent transparent var(--blue);transform:rotate(-20deg)}
  .photo{left:426px;top:136px;width:334px;height:334px;border-radius:50%;background:linear-gradient(160deg,#e9e6e2 0%,var(--photo) 55%,#7f8fa6 100%);border:5px solid var(--white)}

  .front-band{left:0;top:389px;width:745px;height:92px;background:linear-gradient(90deg,var(--band) 0%,#214f92 60%,#163f7a 100%)}
  .call-icon{left:35px;top:22px;width:46px;height:46px;border:2.5px solid var(--white);border-radius:50%;display:flex;align-items:center;justify-content:center}
  .call-text{left:90px;top:17px;font-family:var(--head);font-size:19px;line-height:16.5px;color:var(--white);text-transform:uppercase;font-weight:500}
  .call-text b{font-weight:700}
  .call-text .green{color:var(--green);font-weight:700}
  .band-divider{left:289px;top:18px;width:1px;height:56px;background:rgba(255,255,255,.6)}
  .contact-line{display:flex;align-items:center;gap:12px;color:var(--white)}
  .front-phone{left:312px;top:20px;font-family:var(--head);font-weight:700;font-size:21px}
  .front-web{left:312px;top:48px;font-size:12.5px}
  .front-nmls{right:22px;top:66px;font-size:11px;color:var(--white)}

  /* back */
  .back-headline{left:40px;top:18px;font-size:44px;line-height:40px}
  .stamp-box{left:633px;top:29px;width:73px;height:73px;border:1px solid #b8bcc2}
  .topic-icon{width:38px;height:38px;border-radius:50%;background:linear-gradient(180deg,#1f5fa3,#103f75);display:flex;align-items:center;justify-content:center}
  .notice-title{left:87px;top:121px;font-size:12.5px;font-weight:800;color:var(--blue)}
  .notice-list{list-style:none;font-size:9.8px;line-height:12px;color:var(--ink)}
  .notice-list li{position:relative;padding-left:10px;margin-bottom:5px}
  .notice-list li::before{content:"";position:absolute;left:0;top:4px;width:4px;height:4px;border-radius:50%;background:var(--green)}
  .back-divider{left:40px;top:209px;width:352px;height:1px;background:#cfd8c8}
  .qualify{left:87px;top:218px;font-size:10.8px;line-height:15px;font-weight:800;color:var(--blue)}

  .programs-band{left:0;top:257px;width:490px;height:108px}
  .programs-intro{left:38px;top:267px;font-size:12.8px;line-height:17.5px;font-weight:800;color:var(--white)}
  .programs-icon{left:35px;top:307px;width:46px;height:46px;border-radius:50%;background:var(--green);display:flex;align-items:center;justify-content:center}
  .programs-rule{left:93px;top:308px;width:1px;height:44px;background:var(--green)}
  .program{display:flex;align-items:center;gap:8px;font-family:var(--head);font-size:12.8px;font-weight:500;color:var(--white)}
  .tick{width:14px;height:14px;border-radius:50%;background:var(--green);position:relative;flex:none}
  .tick::after{content:"";position:absolute;left:4.5px;top:2.5px;width:3.5px;height:6px;border:solid var(--white);border-width:0 2px 2px 0;transform:rotate(45deg)}

  .contact-panel{left:32px;top:378px;width:600px;height:80px;border-radius:6px;background:linear-gradient(90deg,#e2ecf7 0%,#edf3fa 65%,rgba(255,255,255,0) 100%)}
  .agent-photo{left:36px;top:374px;width:86px;height:86px;border-radius:50%;background:linear-gradient(180deg,#d8d6d2 0%,#3b3b3e 100%);border:2px solid var(--green)}
  .contact-heading{left:137px;top:393px;font-family:var(--head);font-size:18px;font-weight:700;color:var(--navy);text-transform:uppercase;letter-spacing:.3px}
  .contact-heading .green{color:var(--green);font-size:21px}
  .contact-row{display:flex;align-items:center;gap:10px;color:var(--ink)}
  .round-icon{width:24px;height:24px;border-radius:50%;background:var(--band);display:flex;align-items:center;justify-content:center;flex:none}
  .back-phone{left:137px;top:423px;font-family:var(--head);font-size:16px;font-weight:500}
  .contact-sep{left:313px;top:425px;width:1px;height:20px;background:#7f8a99}
  .back-email{left:332px;top:423px;font-family:var(--head);font-size:13.5px;font-weight:500}
  .back-nmls{right:22px;top:429px;font-size:13px;font-weight:800;color:var(--blue)}
</style>
</head>
<body>
<main class="canvas">

  <!-- FRONT -->
  <section class="card card--front" aria-label="Postcard front">
    <h1 class="abs headline" style="left:40px;top:18px">
      <span class="small">Is a</span> <span class="blue">Property Lien</span><br>
      Putting Your Home<br>
      <span class="green">At Risk?</span>
    </h1>
    <p class="abs lien-types">HOA Liens • Tax Liens • Municipal Charges<br>Other Property-Related Liens</p>

    <div class="abs brand" style="left:572px;top:56px;width:160px;font-size:15px">
      <span class="brand__dot" style="width:14px;height:14px"></span>
      <span>Bluegate Lending Partners, Inc.</span>
    </div>

    <div class="abs rule" style="left:40px;top:153px;width:40px"></div>
    <p class="abs intro">You may have options to resolve outstanding<br>liens and <strong>protect your home.</strong></p>

    <div class="abs photo-ring"></div>
    <div class="abs photo" role="img" aria-label="Photo of a worried couple reviewing bills at a coffee table with a laptop"></div>

    <div class="abs benefit-panel"></div>
    <h2 class="abs benefit-title">A Refinance or Home Equity Line<br>of Credit (HELOC) may help you:</h2>
    <ul class="abs benefit-list">
      <li>Pay off qualifying liens</li>
      <li>Access your home’s equity</li>
      <li>Consolidate debt into one<br>manageable payment</li>
      <li>Improve your financial flexibility</li>
      <li>Avoid additional penalties, fees,<br>or collection actions</li>
    </ul>

    <div class="abs urgent">
      <svg width="26" height="30" viewBox="0 0 26 30" aria-hidden="true">
        <path d="M13 1 L24 5 V14 C24 22 19 27 13 29 C7 27 2 22 2 14 V5 Z" fill="none" stroke="#fff" stroke-width="2"/>
        <path d="M7 15 L13 10 L19 15 V21 H7 Z" fill="none" stroke="#fff" stroke-width="1.6"/>
        <circle cx="16" cy="20" r="4" fill="#78bc36"/>
        <path d="M14.3 20 l1.2 1.2 l2.3 -2.4" fill="none" stroke="#fff" stroke-width="1.2"/>
      </svg>
      Don’t wait<br>until the<br>situation<br>becomes<br><span class="green">more difficult.</span>
    </div>

    <div class="abs front-band">
      <div class="abs call-icon">
        <svg width="24" height="24" viewBox="0 0 24 24" aria-hidden="true"><path d="M6.6 2.5 L9.4 6.6 L7.5 9 C8.7 11.6 10.9 13.9 13.6 15.3 L16 13.4 L20.2 16.2 L18.6 20.4 C10.6 20.2 3.6 13.2 3.2 4.3 Z" fill="#fff"/></svg>
      </div>
      <p class="abs call-text"><b>Call today</b> for a<br><span class="green">Confidential review</span><br>of your options.</p>
      <div class="abs band-divider"></div>
      <p class="abs contact-line front-phone">
        <svg width="18" height="20" viewBox="0 0 24 24" aria-hidden="true"><path d="M6.6 2.5 L9.4 6.6 L7.5 9 C8.7 11.6 10.9 13.9 13.6 15.3 L16 13.4 L20.2 16.2 L18.6 20.4 C10.6 20.2 3.6 13.2 3.2 4.3 Z" fill="#fff"/></svg>
        (800) 647-2915 x 42
      </p>
      <p class="abs contact-line front-web">
        <svg width="18" height="18" viewBox="0 0 20 20" aria-hidden="true"><g fill="none" stroke="#fff" stroke-width="1.3"><circle cx="10" cy="10" r="8.5"/><ellipse cx="10" cy="10" rx="3.8" ry="8.5"/><path d="M1.5 10 H18.5 M3 5.5 H17 M3 14.5 H17"/></g></svg>
        www.bluegatelendco.com
      </p>
      <p class="abs front-nmls">NMLS #381640</p>
    </div>
  </section>

  <!-- BACK -->
  <section class="card card--back" aria-label="Postcard back">
    <h1 class="abs headline back-headline">Your Home Equity<br>Could Be The <span class="green">Solution</span></h1>
    <div class="abs rule" style="left:40px;top:107px;width:111px"></div>

    <div class="abs brand" style="left:470px;top:52px;width:130px;font-size:13.5px">
      <span class="brand__dot" style="width:12px;height:12px"></span>
      <span>Bluegate Lending Partners, Inc.</span>
    </div>
    <div class="abs stamp-box" aria-hidden="true"></div>

    <div class="abs topic-icon" style="left:38px;top:119px">
      <svg width="20" height="20" viewBox="0 0 20 20" aria-hidden="true"><g fill="none" stroke="#fff" stroke-width="1.2"><rect x="3" y="2" width="11" height="15" rx="1"/><path d="M6 6 H11 M6 9 H11 M6 12 H9"/><circle cx="15" cy="14" r="3"/></g></svg>
    </div>
    <h2 class="abs notice-title">If you have received notices regarding:</h2>
    <ul class="abs notice-list" style="left:88px;top:145px;width:140px">
      <li>Delinquent Property Taxes</li>
      <li>HOA or Condo Association Assessments</li>
      <li>Municipal Utility Liens</li>
    </ul>
    <ul class="abs notice-list" style="left:246px;top:145px;width:130px">
      <li>Special Assessments</li>
      <li>Other Property-Related Obligations</li>
    </ul>
    <div class="abs back-divider"></div>

    <div class="abs topic-icon" style="left:38px;top:213px">
      <svg width="22" height="16" viewBox="0 0 22 16" aria-hidden="true"><g fill="none" stroke="#fff" stroke-width="1.2"><rect x="1" y="2" width="20" height="12" rx="1"/><circle cx="11" cy="8" r="3.5"/></g><text x="11" y="10.3" font-size="5.5" text-anchor="middle" fill="#fff" font-family="Arial">$</text></svg>
    </div>
    <p class="abs qualify">You may qualify for financing options designed to<br>help satisfy those obligations and bring your property current.</p>

    <svg class="abs programs-band" viewBox="0 0 490 108" preserveAspectRatio="none" aria-hidden="true">
      <path d="M0 0 H437 C452 40 468 80 485 108 H0 Z" fill="#0c2a55"/>
    </svg>
    <p class="abs programs-intro">Our experienced mortgage professionals can review your<br>situation and discuss available programs, including:</p>
    <div class="abs programs-icon">
      <svg width="28" height="26" viewBox="0 0 28 26" aria-hidden="true"><g fill="none" stroke="#fff" stroke-width="1.4"><path d="M6 11 L14 4 L22 11 M8 10 V17 H20 V10"/><path d="M2 20 C6 18 9 18 13 20 H19 L26 16"/></g><text x="14" y="15.5" font-size="7" text-anchor="middle" fill="#fff" font-family="Arial">$</text></svg>
    </div>
    <div class="abs programs-rule"></div>
    <p class="abs program" style="left:107px;top:313px"><span class="tick"></span>Cash-Out Refinancing</p>
    <p class="abs program" style="left:107px;top:335px"><span class="tick"></span>Home Equity Lines of Credit (HELOCs)</p>
    <p class="abs program" style="left:313px;top:313px"><span class="tick"></span>Home Equity Loans</p>
    <p class="abs program" style="left:313px;top:335px"><span class="tick"></span>Debt Consolidation Solutions</p>

    <div class="abs contact-panel"></div>
    <div class="abs agent-photo" role="img" aria-label="Portrait photo of loan officer Marcus Delaney"></div>
    <p class="abs contact-heading">Contact <span class="green">Marcus Delaney</span> Today!</p>
    <p class="abs contact-row back-phone">
      <span class="round-icon"><svg width="13" height="13" viewBox="0 0 24 24" aria-hidden="true"><path d="M6.6 2.5 L9.4 6.6 L7.5 9 C8.7 11.6 10.9 13.9 13.6 15.3 L16 13.4 L20.2 16.2 L18.6 20.4 C10.6 20.2 3.6 13.2 3.2 4.3 Z" fill="#fff"/></svg></span>
      (800) 647-2915 x42
    </p>
    <div class="abs contact-sep"></div>
    <p class="abs contact-row back-email">
      <span class="round-icon"><svg width="13" height="10" viewBox="0 0 14 10" aria-hidden="true"><g fill="none" stroke="#fff" stroke-width="1.2"><rect x="0.7" y="0.7" width="12.6" height="8.6" rx="1"/><path d="M1 1 L7 6 L13 1"/></g></svg></span>
      mdelaney@bluegatelendco.com
    </p>
    <p class="abs back-nmls">NMLS #57308</p>
  </section>

</main>
</body>
</html>
```